Modern home page design for insurance and investment business

- The design should be based around the attached HPID (home page information design) called KTW HPID. The table boxes are just for approximate placement of information – you DON'T have to make it look exactly like this.
- Information only is in orange text. Copy to go on the design in black text. Some instructions are in the HPID. Please be creative! You don’t have to use the exact images provided if you have a better idea.

- The design needs to be clean and spacious. Please use the colours from the logos in the website design. Lots of white too.

I've attached home page gallery example photos. You can use any of these photos or something similar with the words from one of the photos.

- Expected standard of design examples: (Please DO NOT copy these exactly – they are just examples)
http://www.harbourvane.co.nz/
https://www.brightkeel.co.nz/
http://sandorelcover.co.nz/homepage/

Width of content will be 1100 pixels when implemented as a web page. Header height (without nav bar) 150-160 pixels.

The winning PSD file will have to be provided as follows…
1. Canvas size of 2000px x 2000px - 72ppi in Adobe Photoshop (CS5 compatible)
2. Width of content section is 1100px wide - centered in the canvas
3. Any button rollovers/hovers in the PSD as hidden layers.
4. All fonts used must be Google fonts (except for the fonts in the header at the top of the page).
5. You will need to supply the chosen home page plus one example page (example page as a style guide for how all other pages will look). Example page is only the header and navigational bar at the top, an empty sector in the middle with a column (180 px wide) which can be left or right aligned which means the main sector is 920 pixels wide, and then the footer at the bottom of the page.

```html
<!DOCTYPE html>
<html lang="en">
<head>
<meta charset="utf-8">
<title>KTW – Home</title>
<link href="https://fonts.googleapis.com/css2?family=Arimo:wght@400;700&display=swap" rel="stylesheet">
<style>
:root{
  --stage:#4d7ba6;
  --navy:#0b3d75;
  --footer:#3a67a8;
  --footer-line:#d8e2f0;
  --ink:#1a1a1a;
  --muted:#777;
  --field:#e3e3e3;
  --white:#ffffff;
  --page:#fbfbfb;
}
*{box-sizing:border-box;margin:0;padding:0}
html,body{width:1200px;height:1200px;overflow:hidden}
body{background:var(--stage);font-family:"Arimo",Arial,sans-serif;color:var(--ink);position:relative}
.page{position:absolute;left:271px;top:85px;width:660px;height:1050px;background:var(--page)}
.site-header{position:absolute;left:0;top:0;width:660px;height:66px;background:var(--white)}
.brand{position:absolute;left:41px;top:18px;font-size:28px;font-weight:700;color:var(--navy);line-height:1}
.search{position:absolute;left:531px;top:8px;width:86px;height:14px;border-bottom:1px solid #e4e4e4}
.search svg{position:absolute;right:0;top:1px}
.main-nav{position:absolute;right:42px;top:38px;display:flex;gap:24px;font-size:8.5px;letter-spacing:.4px;color:var(--navy)}
.main-nav a{color:inherit;text-decoration:none}
.main-nav a.is-active{color:#4a8fd0}
.hero{position:absolute;left:0;top:66px;width:660px;height:200px}
.hero-photo{position:absolute;left:0;top:0;width:425px;height:200px;background:linear-gradient(100deg,#cfd6e2 0%,#eef1f6 45%,#f7f7f9 70%,#c9d0dc 100%)}
.hero-panel{position:absolute;left:425px;top:0;width:235px;height:200px;background:var(--navy);color:var(--white);padding:50px 14px 0 14px}
.hero-panel h1{font-size:19px;font-weight:400;line-height:1.4;letter-spacing:.4px}
.hero-panel p{font-size:8.5px;font-weight:700;line-height:1.6;margin-top:10px}
.hero-dots{position:absolute;left:305px;top:190px;display:flex;gap:3px}
.hero-dots span{width:6px;height:6px;border-radius:50%;background:var(--white)}
.hero-dots span.is-active{background:#4a8fd0}
.section-title{position:absolute;left:0;top:296px;width:660px;text-align:center;font-size:15px;font-weight:400;letter-spacing:.3px}
.stages{position:absolute;left:41px;top:336px;display:flex;gap:9px}
.stage{width:137px}
.stage-photo{height:119px;position:relative}
.stage-photo.young{background:#4b4b4b;color:var(--white);font-size:9px;line-height:1.55;text-align:center;padding:8px 6px}
.stage-photo.family{background:linear-gradient(160deg,#bfd9ee,#7fa9c9)}
.stage-photo.couple{background:linear-gradient(180deg,#5d8fc6,#2f64a0)}
.stage-photo.senior{background:linear-gradient(160deg,#d8d3c6,#a8b58c)}
.stage-label{text-align:center;font-size:9px;font-weight:700;margin-top:7px}
.contact-form{position:absolute;left:41px;top:508px;width:260px}
.contact-form h2,.service h2{font-size:14px;font-weight:400;letter-spacing:.3px}
.field{display:block;width:205px;height:25px;border:1px solid var(--field);background:var(--white);font-size:7.5px;color:#aaa;padding:7px 4px;margin-top:12px}
.field:first-of-type{margin-top:8px}
.field.message{width:248px;height:72px;margin-top:13px}
.send{position:absolute;left:0;top:263px;width:56px;height:21px;background:var(--footer);color:var(--white);font-size:9px;letter-spacing:.5px;display:flex;align-items:center;justify-content:center}
.service{position:absolute;left:329px;width:273px}
.service.insurance{top:508px}
.service.investment{top:642px}
.service p{font-size:8px;line-height:1.35;color:var(--muted);text-align:justify;margin-top:8px}
.more{display:flex;justify-content:flex-end;align-items:center;gap:4px;font-size:7.5px;color:var(--navy);margin-top:10px}
.site-footer{position:absolute;left:0;top:819px;width:660px;height:209px;background:var(--footer);color:var(--white);font-size:7.5px}
.footer-col{position:absolute;top:10px}
.footer-col h3{font-size:8.5px;font-weight:700;margin-bottom:8px}
.footer-col ul{list-style:none}
.footer-col li{margin-bottom:6px}
.footer-col li.sub{padding-left:7px}
.footer-col li.sub::before,.bullets li::before{content:"● ";font-size:5px;vertical-align:middle}
.col-links{left:41px}
.col-stages{left:148px}
.col-stages li{margin-bottom:13px}
.col-products{left:317px}
.col-products .group{margin:0 0 6px 8px}
.col-products .bullets{padding-left:16px}
.col-contact{left:454px;width:170px}
.contact-line{display:flex;gap:6px;align-items:flex-start;line-height:1.45;margin-bottom:12px}
.map{width:161px;height:64px;background:#dcdad5;margin-top:4px}
.social{display:flex;align-items:center;gap:5px;margin-top:7px}
.social span.circle{width:12px;height:12px;border-radius:50%;background:var(--white)}
.copyright{position:absolute;left:0;top:1028px;width:660px;height:22px;background:var(--footer);border-top:1px solid var(--footer-line);color:var(--white);font-size:7.5px;padding:5px 41px}
</style>
</head>
<body>
<div class="page">
  <header class="site-header">
    <div class="brand">KTW</div>
    <div class="search"><svg width="9" height="9" viewBox="0 0 10 10"><circle cx="4" cy="4" r="3" fill="none" stroke="#bbb" stroke-width="1.2"/><line x1="6.3" y1="6.3" x2="9" y2="9" stroke="#bbb" stroke-width="1.2"/></svg></div>
    <nav class="main-nav"><a class="is-active" href="#">HOME</a><a href="#">ABOUT</a><a href="#">INSURANCES</a><a href="#">INVESTMENTS</a><a href="#">FAQS</a><a href="#">CONTACT</a></nav>
  </header>

  <section class="hero">
    <div class="hero-photo" role="img" aria-label="Young couple lying together smiling at a laptop"></div>
    <div class="hero-panel">
      <h1>Helping you focus on your future...</h1>
      <p>Lorem Ipsum is simply dummy text of the printing and typesetting industry</p>
    </div>
    <div class="hero-dots"><span class="is-active"></span><span></span><span></span><span></span></div>
  </section>

  <h2 class="section-title">What life stage are you at?</h2>
  <div class="stages">
    <div class="stage"><div class="stage-photo young" role="img" aria-label="Young adult photo with life stage questions overlaid">18-30 life stage<br><br>- Should I start financial planning now?<br>- What insurances do we need?<br>- What is the best way to</div><div class="stage-label">18-30 years</div></div>
    <div class="stage"><div class="stage-photo family" role="img" aria-label="Smiling family of four outdoors"></div><div class="stage-label">30-45 years</div></div>
    <div class="stage"><div class="stage-photo couple" role="img" aria-label="Middle-aged couple embracing by the sea"></div><div class="stage-label">45-65 years</div></div>
    <div class="stage"><div class="stage-photo senior" role="img" aria-label="Retired couple sharing a drink at a table"></div><div class="stage-label">65+ years</div></div>
  </div>

  <form class="contact-form">
    <h2>Fill in the form and we’ll be in touch</h2>
    <span class="field">First name</span>
    <span class="field">Last name</span>
    <span class="field">Email</span>
    <span class="field">Contact phone</span>
    <span class="field message">Message</span>
    <span class="send">SEND</span>
  </form>

  <article class="service insurance">
    <h2>Insurance</h2>
    <p>An overview of insurance from the point of view of benefits to the customer of working with KTW will be in this space.....Relevant keywords such as the types of insurances e.g. life insurance, travel insurance etc will be mentioned... Should be inviting to both new and current customers....</p>
    <div class="more"><svg width="9" height="9" viewBox="0 0 10 10"><path d="M2 5h6M5 2l3 3-3 3" fill="none" stroke="#0b3d75" stroke-width="1.4"/></svg>Find out more</div>
  </article>
  <article class="service investment">
    <h2>Investment</h2>
    <p>An overview of investments from the point of view of benefits to the customer of working with KTW will be in this space.....Relevant keywords such as financial planning, investment advice and RetireStart will be mentioned...Should be inviting to both new and current customers....</p>
    <div class="more"><svg width="9" height="9" viewBox="0 0 10 10"><path d="M2 5h6M5 2l3 3-3 3" fill="none" stroke="#0b3d75" stroke-width="1.4"/></svg>Find out more</div>
  </article>

  <footer class="site-footer">
    <div class="footer-col col-links"><ul>
      <li>Home</li><li>About</li><li class="sub">Meet the Team</li><li class="sub">Testimonials</li>
      <li style="margin-top:12px">What We Do</li><li style="margin-top:12px">FAQs</li><li>Consultation</li></ul></div>
    <div class="footer-col col-stages"><h3>What Life Stage are You?</h3><ul class="bullets">
      <li>Life stage 18-30 years</li><li>Life stage 30-45 years</li><li>Life stage 45-65 years</li><li>Life stage 65+ years</li></ul></div>
    <div class="footer-col col-products"><h3>Products/Services</h3>
      <div class="group">Insurance</div>
      <ul class="bullets"><li>Life insurance</li><li>Trauma insurance</li><li>Disablement cover</li><li>Income protection</li><li>Health insurance</li><li>Business insurance</li><li>Fire &amp; General</li><li>Travel insurance</li></ul>
      <div class="group" style="margin-top:10px">Investment</div>
      <ul class="bullets"><li>Travel insurance</li></ul></div>
    <div class="footer-col col-contact"><h3>Contact</h3>
      <div class="contact-line"><svg width="8" height="10" viewBox="0 0 8 10"><path d="M4 0a3.5 3.5 0 0 0-3.5 3.5C.5 6 4 10 4 10s3.5-4 3.5-6.5A3.5 3.5 0 0 0 4 0z" fill="#fff"/><circle cx="4" cy="3.5" r="1.3" fill="#3a67a8"/></svg><span>128 Harbour Rd, Ashby<br>New Zealand</span></div>
      <div class="contact-line"><svg width="9" height="9" viewBox="0 0 10 10"><circle cx="5" cy="5" r="4.2" fill="none" stroke="#fff" stroke-width="1.2"/><path d="M5 2.5V5h2" fill="none" stroke="#fff" stroke-width="1.1"/></svg><span>Office Hours: 8.30 – 5pm</span></div>
      <div class="contact-line"><svg width="9" height="9" viewBox="0 0 10 10"><path d="M2 0.8l2 2.2-1 1.2c.6 1.2 1.6 2.2 2.8 2.8l1.2-1 2.2 2-1.2 1.6C4.8 9.2.8 5.2.4 2z" fill="#fff"/></svg><span>After Hours: Please phone<br>0800 555 0142 | 06 555 0142</span></div>
      <div class="map" role="img" aria-label="Street map showing the office location"></div>
      <div class="social"><span class="circle"></span>Connect to Circlebook</div>
    </div>
  </footer>
  <div class="copyright">Copyright © 2014 Insurance and Investment business - All Rights Reserved.</div>
</div>
</body>
</html>
```